Rent a Velvet needs a Stunning web design

Rent a Velvet is an upmarket agency in Sydney that has lingerie waitresses for events.

Rent a Velvet is looking for a website design that is as sexy and sophisticated as the ladies who work for them!

The design mustn't be cluttered, tacky or pornographic. What I'm looking for is something better than the industry leader www.glimmerdolls.com.au Something classy, sexy and different.

When designing please suggest a CMS, we already use wordpress but are open to suggestions.

We will need a home page that incorporates a feed from a blog and/or social media (please make suggestions and use your discretion as a designer, however we'd like to approve what goes into the feed before it goes in.) The home page could also have a list of our services, but if not we will need a services page. Our Services include:
Lingerie waitressing at events
Lingerie waitresses to help dress the groom pre wedding.
Bucks parties

We have a logo that we'd like incorporated into the design and have attached it.

We will also need a portfolio page for the ladies, This is not to be cluttered, tacky or pornographic. It needs to be classy.

We will also need a "Contact us" page and were thinking that this could potentially also be a "Ask for a quote on your event" page. I.e. have a regular "Contact us" form but have alternate fields if they tick the "I want a quote" box. Alternatively you could have two parts to the contact us page. One that is a regular form and one that has a "Your requirements" box.

Again please use your discretion when designing these, if it's too cluttered it won't work. If it looks tacky, don't do it. If you have suggestions make them.

Target Market(s)

Males between the ages of 18 - 45

Industry/Entity Type

Industry

Requirements
Must have
• Must incorporate our logo.

```html
<!DOCTYPE html>
<html lang="en">
<head>
<meta charset="utf-8">
<title>Rent a Velvet</title>
<link href="https://fonts.googleapis.com/css2?family=Oswald:wght@500&family=PT+Sans:wght@400;700&display=swap" rel="stylesheet">
<style>
:root{
  --red:#d41f45;
  --red-deep:#b3163a;
  --red-band:#cf2a49;
  --paper:#efeeee;
  --ink:#222;
  --dark:#262626;
  --dark-2:#303030;
  --footer-text:#8a8a8a;
  --white:#fff;
}
*{margin:0;padding:0;box-sizing:border-box}
h1,h2,h3,h4{font-weight:400}
html,body{width:746px;height:1200px;overflow:hidden}
body{position:relative;background:var(--paper);font-family:"PT Sans",sans-serif;color:var(--ink)}
.abs{position:absolute}

/* header */
.header-band{left:0;top:0;width:746px;height:190px;background:
  radial-gradient(circle at 18% 8%,rgba(255,255,255,.18) 0,rgba(255,255,255,0) 70px),
  radial-gradient(circle at 58% 5%,rgba(180,10,40,.35) 0,rgba(180,10,40,0) 60px),
  radial-gradient(circle at 90% 20%,rgba(255,255,255,.10) 0,rgba(255,255,255,0) 90px),
  linear-gradient(180deg,#d43a55 0,var(--red-band) 55%,#c11f40 100%)}
.brand{left:72px;top:30px;font-size:30px;font-weight:700;color:var(--white);white-space:nowrap;display:flex;align-items:center;gap:8px}
.brand-dot{width:12px;height:12px;border-radius:50%;background:var(--white)}
.social{top:12px;width:16px;height:16px;border:1px solid #9a9a9a;background:#f4f4f4;border-radius:2px}
.social svg{display:block;margin:2px auto 0}
.search{left:563px;top:54px;width:109px;height:17px;background:var(--white);border-radius:3px;font-size:8px;color:#333;padding:4px 6px}
.search svg{position:absolute;right:5px;top:3px}
.nav{left:66px;top:86px;width:614px;height:24px}
.nav-item{top:92px;font-size:12px;color:var(--white);transform:translateX(-50%);white-space:nowrap}
.nav-sep{top:88px;width:1px;height:20px;background:rgba(255,255,255,.25)}

/* hero */
.hero{left:64px;top:123px;width:620px;height:323px;background:
  radial-gradient(ellipse 90px 120px at 30% 38%,rgba(205,170,130,.55) 0,rgba(205,170,130,0) 100%),
  radial-gradient(ellipse 60px 30px at 27% 74%,rgba(170,30,50,.55) 0,rgba(170,30,50,0) 100%),
  radial-gradient(ellipse 140px 80px at 60% 90%,rgba(110,55,55,.45) 0,rgba(110,55,55,0) 100%),
  linear-gradient(90deg,#2a201c 0,#3b2d27 30%,#2a211e 60%,#1b1614 100%);box-shadow:0 10px 14px -8px rgba(0,0,0,.5)}
.hero-title{left:386px;top:202px;font-family:"Oswald",sans-serif;font-weight:500;font-size:22px;color:#f0405a;letter-spacing:.2px}
.hero-copy{left:387px;top:235px;width:260px;font-size:9.3px;line-height:15px;color:#f2f2f2}
.dot{top:435px;width:6px;height:6px;border-radius:50%;background:#ddd}
.dot.active{background:var(--red)}

/* gallery */
.welcome{left:66px;top:466px;font-size:12px;color:var(--red)}
.section-title{font-size:11px;color:var(--ink);text-transform:uppercase}
.card{top:514px;width:146px;height:180px}
.card-photo{width:146px;height:145px}
.card-label{height:35px;background:var(--red);text-align:center;color:var(--white);padding-top:6px}
.card-label strong{display:block;font-weight:400;font-size:11.5px;color:#2a0a10}
.card-label span{display:block;font-size:6.5px;margin-top:1px}

/* video */
.video-frame{left:70px;top:733px;width:311px;height:217px;background:#ddd;padding:4px}
.video-still{width:303px;height:209px;background:
  radial-gradient(ellipse 40px 90px at 72% 45%,rgba(235,225,215,.9) 0,rgba(235,225,215,0) 100%),
  radial-gradient(ellipse 90px 30px at 55% 88%,rgba(215,195,150,.5) 0,rgba(215,195,150,0) 100%),
  linear-gradient(90deg,#c9c4bc 0,#dcd7d0 35%,#ebe8e3 60%,#d6d0c8 100%);position:relative}
.play{position:absolute;left:129px;top:87px;width:36px;height:36px;border-radius:50%;background:rgba(60,60,60,.75)}
.ratings{left:394px;top:743px;font-size:11px}
.share-btn{top:776px;height:13px;font-size:7px;font-weight:700;color:var(--white);padding:2px 5px;border-radius:2px}
.share-count{top:776px;height:13px;font-size:7px;padding:2px 3px;border:1px solid #bbb;background:#f7f7f7}
.video-title{left:398px;top:804px;font-size:12px;color:var(--red)}
.video-copy{left:398px;top:826px;width:270px;font-size:6.9px;line-height:15px;color:#333}

/* footer */
.footer{left:0;top:960px;width:746px;height:216px;background:var(--dark)}
.footer-title{top:976px;font-size:11.5px;color:#e4e4e4;text-transform:uppercase}
.date{left:86px;width:44px;height:38px;background:var(--red);border:2px solid var(--white);color:var(--white);text-align:center}
.date b{display:block;font-weight:400;font-size:16px;line-height:18px;margin-top:2px}
.date small{display:block;font-size:6px}
.post{width:140px;font-size:7.5px;line-height:11px;color:var(--footer-text)}
.post em{display:block;font-style:normal;font-size:8px;color:var(--red)}
.field{left:338px;width:131px;background:var(--dark-2);font-size:7px;color:#ddd;padding:5px 4px}
.field b{font-weight:700}
.send{left:362px;top:1122px;width:76px;height:16px;background:var(--red);border-radius:2px;color:var(--white);font-size:8px;text-align:center;line-height:16px}
.thumb{left:522px;width:57px;height:40px;border:2px solid var(--white)}

.bottom-bar{left:0;top:1176px;width:746px;height:24px;background:var(--red-deep)}
.bottom-link{top:1183px;font-size:7.5px;color:var(--white);text-transform:uppercase}
.bottom-link.current{color:#f3a0ae}
.copyright{left:566px;top:1183px;font-size:7.5px;color:var(--white)}
</style>
</head>
<body>

<div class="abs header-band"></div>
<div class="abs brand"><span>Rent a Velvet</span><span class="brand-dot"></span></div>

<div class="abs social" style="left:618px" aria-label="Email">
  <svg width="10" height="10" viewBox="0 0 10 10"><rect x=".5" y="2" width="9" height="6.5" fill="none" stroke="#444" stroke-width="1"/><polyline points=".8,2.3 5,5.8 9.2,2.3" fill="none" stroke="#444" stroke-width="1"/></svg>
</div>
<div class="abs social" style="left:637px" aria-label="Chat">
  <svg width="10" height="10" viewBox="0 0 10 10"><path d="M1 1.5h8v5H4.5L2 9V6.5H1z" fill="none" stroke="#444" stroke-width="1"/></svg>
</div>
<div class="abs social" style="left:657px" aria-label="Share">
  <svg width="10" height="10" viewBox="0 0 10 10"><circle cx="2.2" cy="5" r="1.4" fill="#444"/><circle cx="7.8" cy="2" r="1.4" fill="#444"/><circle cx="7.8" cy="8" r="1.4" fill="#444"/><path d="M2.2 5L7.8 2M2.2 5L7.8 8" stroke="#444" stroke-width="1"/></svg>
</div>

<div class="abs search">Search
  <svg width="10" height="10" viewBox="0 0 10 10"><circle cx="4" cy="4" r="3" fill="none" stroke="#777" stroke-width="1.3"/><line x1="6.2" y1="6.2" x2="9.3" y2="9.3" stroke="#777" stroke-width="1.6"/></svg>
</div>

<svg class="abs nav" viewBox="0 0 614 24" preserveAspectRatio="none">
  <polygon points="0,0 614,0 604,12 614,24 0,24 10,12" fill="#e5314f"/>
</svg>
<span class="abs nav-item" style="left:136px">Home</span>
<span class="abs nav-sep" style="left:161px"></span>
<span class="abs nav-item" style="left:197px">About us</span>
<span class="abs nav-sep" style="left:230px"></span>
<span class="abs nav-item" style="left:289px">Lingerie waitresses</span>
<span class="abs nav-sep" style="left:346px"></span>
<span class="abs nav-item" style="left:374px">Events</span>
<span class="abs nav-sep" style="left:402px"></span>
<span class="abs nav-item" style="left:424px">Blog</span>
<span class="abs nav-sep" style="left:446px"></span>
<span class="abs nav-item" style="left:474px">Videos</span>
<span class="abs nav-sep" style="left:502px"></span>
<span class="abs nav-item" style="left:530px">Gallery</span>
<span class="abs nav-sep" style="left:557px"></span>
<span class="abs nav-item" style="left:597px">Contact Us</span>

<div class="abs hero" role="img" aria-label="Photo of a model in red lingerie seated in a dim bedroom"></div>
<h1 class="abs hero-title">LOREM IPSUM PASSAGE</h1>
<p class="abs hero-copy">Sed ut perspiciatis unde omnis iste natus error sit voluptatem accusantium doloremque laudantium, totam rem aperiam, eaque ipsa quae ab illo inventore veritatis et quasi architecto beatae vitae dicta sunt explicabo. Nemo enim ipsam voluptatem quia voluptas sit aspernatur aut odit aut fugit, sed quia</p>
<span class="abs dot" style="left:351px"></span>
<span class="abs dot" style="left:363px"></span>
<span class="abs dot" style="left:376px"></span>
<span class="abs dot active" style="left:389px"></span>

<h2 class="abs welcome">WELCOME TO RENT A VELVET</h2>
<h3 class="abs section-title" style="left:69px;top:493px">Lingeries Gallery</h3>

<div class="abs card" style="left:66px">
  <div class="card-photo" role="img" aria-label="Model in black lace lingerie" style="background:radial-gradient(ellipse 50px 60px at 55% 35%,rgba(240,215,185,.8) 0,rgba(240,215,185,0) 100%),radial-gradient(ellipse 60px 35px at 65% 85%,rgba(30,25,25,.7) 0,rgba(30,25,25,0) 100%),linear-gradient(135deg,#d6bd98,#9c7f62)"></div>
  <div class="card-label"><strong>NAME OF THE PRODUCT</strong><span>Click here to view more details</span></div>
</div>
<div class="abs card" style="left:223px">
  <div class="card-photo" role="img" aria-label="Model in ivory corset" style="background:radial-gradient(ellipse 40px 70px at 50% 60%,rgba(215,205,190,.8) 0,rgba(215,205,190,0) 100%),radial-gradient(ellipse 25px 20px at 45% 18%,rgba(80,60,50,.5) 0,rgba(80,60,50,0) 100%),linear-gradient(90deg,#8e8a85,#b8b4ae 60%,#9a958f)"></div>
  <div class="card-label"><strong>NAME OF THE PRODUCT</strong><span>Click here to view more details</span></div>
</div>
<div class="abs card" style="left:379px">
  <div class="card-photo" role="img" aria-label="Model in red polka dot bra" style="background:radial-gradient(ellipse 45px 22px at 50% 80%,rgba(200,40,50,.7) 0,rgba(200,40,50,0) 100%),radial-gradient(ellipse 45px 60px at 50% 40%,rgba(200,170,145,.6) 0,rgba(200,170,145,0) 100%),linear-gradient(135deg,#a39d97,#77716b)"></div>
  <div class="card-label"><strong>NAME OF THE PRODUCT</strong><span>Click here to view more details</span></div>
</div>
<div class="abs card" style="left:536px">
  <div class="card-photo" role="img" aria-label="Model in dark lingerie and open shirt" style="background:radial-gradient(ellipse 40px 50px at 60% 40%,rgba(210,170,140,.55) 0,rgba(210,170,140,0) 100%),radial-gradient(ellipse 50px 40px at 50% 85%,rgba(20,15,15,.7) 0,rgba(20,15,15,0) 100%),linear-gradient(90deg,#9a7c60,#4a3a32 60%,#2e2521)"></div>
  <div class="card-label"><strong>NAME OF THE PRODUCT</strong><span>Click here to view more details</span></div>
</div>

<h3 class="abs section-title" style="left:70px;top:709px">Videos</h3>
<div class="abs video-frame">
  <div class="video-still" role="img" aria-label="Video still of a model in white lingerie by a doorway">
    <svg class="play" viewBox="0 0 36 36"><polygon points="14,11 26,18 14,25" fill="#eee"/></svg>
  </div>
</div>

<div class="abs ratings">Ratings :
  <svg width="62" height="11" viewBox="0 0 62 11" style="vertical-align:-1px">
    <defs><polygon id="star" points="5.5,0 7,3.8 11,4 7.8,6.6 9,10.6 5.5,8.3 2,10.6 3.2,6.6 0,4 4,3.8"/></defs>
    <use href="#star" x="0" fill="#111"/>
    <use href="#star" x="12" fill="#ccc"/>
    <svg x="12" width="6" height="11"><use href="#star" fill="#111"/></svg>
    <use href="#star" x="24" fill="#ccc"/>
    <use href="#star" x="36" fill="#ccc"/>
    <use href="#star" x="48" fill="#ccc"/>
  </svg>
</div>
<span class="abs share-btn" style="left:398px;background:#3b8fc9">Tweet</span>
<span class="abs share-count" style="left:438px">5</span>
<span class="abs share-btn" style="left:457px;background:#4a68a8">Share</span>
<span class="abs share-count" style="left:497px">52</span>
<span class="abs share-btn" style="left:521px;background:#2d8a3e">Share</span>
<span class="abs share-count" style="left:563px">110</span>

<h3 class="abs video-title">VIDEO DISCRIPTION</h3>
<p class="abs video-copy">Lorem Ipsum is simply dummy text of the printing and typesetting industry. Lorem Ipsum has been the industry's standard dummy text ever since the 1500s, when an unknown printer took a galley of type and scrambled it to make a type specimen book. It has survived not only five centuries<br>Sed ut perspiciatis unde omnis iste natus error sit voluptatem accusantium doloremque laudantium, totam rem aperiam, eaque ipsa quae ab illo inventore veritatis et quasi architecto beatae</p>

<footer>
<div class="abs footer"></div>

<h4 class="abs footer-title" style="left:86px">Latest News</h4>
<div class="abs date" style="top:998px"><b>22</b><small>Jun - 2012</small></div>
<p class="abs post" style="left:139px;top:997px"><em>This is a sample Post 1</em>Lorem ipsum dolor sit amet, consect-etur adipisicing elit, sed do eiusmod tempor</p>
<div class="abs date" style="top:1050px"><b>22</b><small>Jun - 2012</small></div>
<p class="abs post" style="left:139px;top:1049px"><em>This is a sample Post 1</em>Lorem ipsum dolor sit amet, consect-etur adipisicing elit, sed do eiusmod tempor</p>
<div class="abs date" style="top:1102px"><b>22</b><small>Jun - 2012</small></div>
<p class="abs post" style="left:139px;top:1101px"><em>This is a sample Post 1</em>Lorem ipsum dolor sit amet, consect-etur adipisicing elit, sed do eiusmod tempor</p>

<h4 class="abs footer-title" style="left:339px">Get in Touch</h4>
<div class="abs field" style="top:1000px;height:20px"><b>Email</b> (required)</div>
<div class="abs field" style="top:1023px;height:20px"><b>Email</b> (required)</div>
<div class="abs field" style="top:1046px;height:68px"><b>Message</b> (required)</div>
<div class="abs send">Send Message</div>

<h4 class="abs footer-title" style="left:521px;top:977px">Latest Posts</h4>
<div class="abs thumb" style="top:998px;background:radial-gradient(circle at 45% 50%,#e0401f 0,#9a1a0e 55%,#3a0704 100%)" role="img" aria-label="Red fruit thumbnail"></div>
<p class="abs post" style="left:584px;top:997px;width:95px"><em>This is a sample Post 1</em>Lorem ipsum dolor sit amet, consectetuer adipiscing elit, sed diam nonummy nibh...</p>
<div class="abs thumb" style="top:1058px;background:radial-gradient(circle at 60% 45%,#c8c8c8 0,#5a5a5a 45%,#151515 100%)" role="img" aria-label="Black and white rose thumbnail"></div>
<p class="abs post" style="left:584px;top:1057px;width:95px"><em>This is a sample Post 1</em>Lorem ipsum dolor sit amet, consectetuer adipiscing elit, sed diam nonummy nibh...</p>
<div class="abs thumb" style="top:1118px;background:radial-gradient(circle at 45% 50%,#d8231d 0,#b51812 40%,#f2f2f2 70%)" role="img" aria-label="Strawberry thumbnail"></div>
<p class="abs post" style="left:584px;top:1117px;width:95px"><em>This is a sample Post 1</em>Lorem ipsum dolor sit amet, consectetuer adipiscing elit, sed diam nonummy nibh...</p>

<div class="abs bottom-bar"></div>
<span class="abs bottom-link current" style="left:87px">Home</span>
<span class="abs bottom-link" style="left:122px">About us</span>
<span class="abs bottom-link" style="left:171px">Lingerie waitresses</span>
<span class="abs bottom-link" style="left:257px">Events</span>
<span class="abs bottom-link" style="left:296px">Blog</span>
<span class="abs bottom-link" style="left:329px">Videos</span>
<span class="abs bottom-link" style="left:367px">Gallery</span>
<span class="abs bottom-link" style="left:411px">Contact us</span>
<span class="abs copyright">© 2012.www.rentavelvet.com</span>
</footer>

</body>
</html>
```